University Chair needs a Flyer for inviting participants to a Podcast series

We need a flyer design for a new podcast series. The Centre for Market Structure Studies at the business university KPL (www.kpl.edu) will invite selected contacts to participate in a new podcast series. The flyer should first gain the participants attention and interest and second inform them about the activity. The overall theme is on "Strategy, Analytics, Economics and Leadership". Please refer to the flyer.pdf in the attached files.

Industry/Entity Type

Business

Font styles to use
Serif
Sans Serif

```html
<!DOCTYPE html>
<html lang="en">
<head>
<meta charset="utf-8">
<title>Centre for Market Structure Studies – Flyer</title>
<link href="https://fonts.googleapis.com/css2?family=Noticia+Text:wght@700&family=Quattrocento+Sans:wght@400;700&family=Arimo:wght@400;700&display=swap" rel="stylesheet">
<style>
  :root {
    --brand-blue: #2d4593;
    --brand-stripe: #8395da;
    --slate-blue: #3d5e84;
    --slate-deep: #23395a;
    --header-navy: #1f3252;
    --charcoal: #2a2a2a;
    --title-grey: #3a3a3a;
    --text-dark: #2e2e2e;
    --white: #ffffff;
    --canvas: #ebebeb;
  }
  * { box-sizing: border-box; margin: 0; padding: 0; }
  html, body { width: 1200px; height: 1085px; overflow: hidden; }
  body { background: var(--canvas); position: relative; font-family: "Quattrocento Sans", sans-serif; }

  .panel { position: absolute; width: 244px; height: 517px; overflow: hidden; }
  .layer { position: absolute; left: 0; top: 0; width: 100%; height: 100%; }
  .photo { position: absolute; left: 0; width: 100%; }

  /* name plate: plain text, one colour, one weight */
  .name-plate { position: absolute; left: 0; width: 100%; text-align: center; font-family: "Quattrocento Sans", sans-serif; font-weight: 400; font-size: 38px; line-height: 1; letter-spacing: 6px; }
  .name-plate.light { color: var(--white); }
  .name-plate.dark { color: #1d1d1d; }

  /* cover */
  .brand-bar { position: absolute; left: 0; top: 0; width: 100%; height: 122px; background: var(--brand-blue); }
  .brand-stripe { position: absolute; left: 0; top: 122px; width: 100%; height: 6px; background: var(--brand-stripe); }
  .cover-title { position: absolute; left: 0; top: 356px; width: 100%; text-align: center; color: var(--white); font-weight: 400; font-size: 27px; line-height: 37px; letter-spacing: 0.5px; }
  .cover-rule { position: absolute; left: 32px; top: 472px; width: 182px; height: 2px; background: #e6e6e6; }

  /* profile */
  .profile-bg { background: linear-gradient(180deg, #d4d4d4 0%, #cfcfcf 40%, #c2c2c2 100%); }
  .serif-title { position: absolute; left: 10px; top: 58px; width: 224px; text-align: center; font-family: "Noticia Text", serif; font-weight: 700; font-size: 25px; line-height: 31px; color: var(--title-grey); }
  .portrait { position: absolute; left: 55px; top: 193px; width: 136px; height: 136px; border-radius: 50%; border: 4px solid var(--white); background: radial-gradient(circle at 50% 40%, #6b5a4e 0%, #3b302b 55%, #1f1c1c 100%); }
  .profile-name { position: absolute; left: 0; top: 352px; width: 100%; text-align: center; color: var(--white); font-size: 16px; letter-spacing: 0.2px; }
  .profile-details { position: absolute; left: 20px; top: 387px; width: 204px; text-align: center; color: var(--white); font-size: 10.2px; line-height: 14.5px; }
  .profile-details .gap { height: 14px; }

  /* text blocks */
  .copy-heading { position: absolute; font-size: 14px; font-weight: 700; }
  .copy-heading.ruled { padding-bottom: 3px; border-bottom: 1px solid currentColor; }
  .copy { position: absolute; font-size: 8.8px; line-height: 12.5px; }
  .on-dark { color: var(--white); }
  .on-light { color: var(--text-dark); }

  .intro-photo { top: 0; height: 300px; background: linear-gradient(160deg, #8c99a6 0%, #4d5966 45%, #2c333c 100%); }

  .inside-lead { background: linear-gradient(90deg, #436589 0%, #2f4c70 60%, var(--slate-deep) 100%); }
  .section-bar { position: absolute; left: 0; top: 0; width: 100%; height: 48px; background: var(--header-navy); color: var(--white); font-family: "Arimo", sans-serif; font-weight: 700; font-size: 12.4px; line-height: 48px; text-align: center; white-space: nowrap; }
  .inside-bg { background: linear-gradient(180deg, #e4e4e4 0%, #d8d8d8 50%, #cfcfcf 100%); }
</style>
</head>
<body>

<!-- Single cover -->
<section class="panel cover" style="left:70px; top:18px;">
  <div class="photo" role="img" aria-label="Photo of the university building with students outside" style="top:128px; height:300px; background:linear-gradient(180deg,#8fb3d6 0%,#b9a88f 45%,#8d7b66 100%);"></div>
  <svg class="layer" viewBox="0 0 244 517" preserveAspectRatio="none" aria-hidden="true">
    <path d="M0,330 Q110,300 244,320 L244,517 L0,517 Z" fill="#7a7a7a" opacity="0.85"/>
    <path d="M0,345 Q120,318 244,338 L244,517 L0,517 Z" fill="#2b2b2b"/>
    <path d="M0,368 Q110,340 244,350 L244,517 L0,517 Z" fill="#3a5b82"/>
    <path d="M0,420 L244,420 L244,517 L0,517 Z" fill="#33506f" opacity="0.6"/>
  </svg>
  <div class="brand-bar"></div>
  <div class="brand-stripe"></div>
  <div class="name-plate light" style="top:44px;">KPL</div>
  <h1 class="cover-title">Economics for<br>Strategic<br>Leaders</h1>
  <div class="cover-rule"></div>
</section>

<!-- Single profile panel -->
<section class="panel profile-bg" style="left:70px; top:545px;">
  <svg class="layer" viewBox="0 0 244 517" preserveAspectRatio="none" aria-hidden="true">
    <path d="M0,200 Q130,170 244,255 L244,517 L0,517 Z" fill="#7d7d7d"/>
    <path d="M0,240 Q120,220 244,300 L244,517 L0,517 Z" fill="#2b2b2b"/>
    <path d="M55,517 Q120,330 244,355 L244,517 Z" fill="#46698f"/>
  </svg>
  <h2 class="serif-title">Centre for Market Structure Studies</h2>
  <div class="portrait" role="img" aria-label="Portrait photo of the professor"></div>
  <p class="profile-name">Prof. Dr. Martin Keller</p>
  <div class="profile-details">
    <p>KPL – Arden School of<br>Management</p>
    <div class="gap"></div>
    <p>Schlossweg 4 D-50210 Talheim</p>
    <p>Mail: mkeller@kpl.edu</p>
    <p>Tel.: +(49) 221 4410 - 180</p>
  </div>
</section>

<!-- Outside spread -->
<section class="panel" style="left:426px; top:18px;">
  <div class="photo intro-photo" role="img" aria-label="Photo of a businessman writing a business plan on glass"></div>
  <svg class="layer" viewBox="0 0 244 517" preserveAspectRatio="none" aria-hidden="true">
    <path d="M0,170 Q130,175 244,225 L244,517 L0,517 Z" fill="#5a5a5a" opacity="0.55"/>
    <path d="M0,290 Q110,262 244,275 L244,517 L0,517 Z" fill="var(--charcoal)"/>
  </svg>
  <h3 class="copy-heading on-dark" style="left:22px; top:310px;">Lorem Ipsum</h3>
  <p class="copy on-dark" style="left:22px; top:338px; width:204px;">Lorem ipsum dolor sit amet, consectetur adipisici elit, sed eiusmod tempor incidunt ut labore et dolore magna aliqua. Ut enim ad minim veniam, quis nostrud exercitation ullamco laboris nisi ut aliquid ex ea commodi consequat. Quis aute iure reprehenderit in voluptate velit esse cillum dolore eu fugiat nulla pariatur. Excepteur sint obcaecat cupiditat non proident, sunt in culpa qui officia deserunt mollit anim id est laborum.</p>
</section>

<section class="panel profile-bg" style="left:670px; top:18px;">
  <svg class="layer" viewBox="0 0 244 517" preserveAspectRatio="none" aria-hidden="true">
    <path d="M0,225 Q130,200 244,250 L244,517 L0,517 Z" fill="#7d7d7d"/>
    <path d="M0,262 Q120,245 244,300 L244,517 L0,517 Z" fill="#2b2b2b"/>
    <path d="M30,517 Q110,340 244,345 L244,517 Z" fill="#46698f"/>
  </svg>
  <h2 class="serif-title" style="top:58px;">Centre for Market Structure Studies</h2>
  <div class="portrait" role="img" aria-label="Portrait photo of the professor" style="top:188px;"></div>
  <p class="profile-name" style="top:345px;">Prof. Dr. Martin Keller</p>
  <div class="profile-details" style="top:380px;">
    <p>KPL – Arden School of<br>Management</p>
    <div class="gap"></div>
    <p>Schlossweg 4 D-50210 Talheim</p>
    <p>Mail: mkeller@kpl.edu</p>
    <p>Tel.: +(49) 221 4410 - 180</p>
  </div>
</section>

<section class="panel cover" style="left:914px; top:18px;">
  <div class="photo" role="img" aria-label="Photo of the university building with students outside" style="top:128px; height:300px; background:linear-gradient(180deg,#8fb3d6 0%,#b9a88f 45%,#8d7b66 100%);"></div>
  <svg class="layer" viewBox="0 0 244 517" preserveAspectRatio="none" aria-hidden="true">
    <path d="M0,300 Q110,305 244,340 L244,517 L0,517 Z" fill="#7a7a7a" opacity="0.85"/>
    <path d="M0,330 Q120,330 244,350 L244,517 L0,517 Z" fill="#2b2b2b"/>
    <path d="M0,350 Q110,335 244,355 L244,517 L0,517 Z" fill="#3a5b82"/>
    <path d="M0,420 L244,420 L244,517 L0,517 Z" fill="#33506f" opacity="0.6"/>
  </svg>
  <div class="brand-bar"></div>
  <div class="brand-stripe"></div>
  <div class="name-plate light" style="top:44px;">KPL</div>
  <h1 class="cover-title">Economics for<br>Strategic<br>Leaders</h1>
  <div class="cover-rule"></div>
</section>

<!-- Inside spread -->
<section class="panel inside-lead" style="left:426px; top:545px;">
  <div class="name-plate light" style="top:42px;">KPL</div>
  <h3 class="copy-heading ruled on-dark" style="left:22px; top:118px;">Lorem Ipsum</h3>
  <p class="copy on-dark" style="left:22px; top:150px; width:204px;">Lorem ipsum dolor sit amet, consectetur adipisici elit, sed eiusmod tempor incidunt ut labore et dolore magna aliqua. Ut enim ad minim veniam, quis nostrud exercitation ullamco laboris nisi ut aliquid ex ea commodi consequat. Quis aute iure reprehenderit in voluptate velit esse cillum dolore eu fugiat nulla pariatur. Excepteur sint obcaecat cupiditat non proident, sunt in culpa qui officia deserunt mollit anim id est laborum.</p>
  <p class="copy on-dark" style="left:22px; top:292px; width:204px;">Lorem ipsum dolor sit amet, consectetur adipisici elit, sed eiusmod tempor incidunt ut labore et dolore magna aliqua. Ut enim ad minim veniam, quis nostrud exercitation ullamco laboris nisi ut aliquid ex ea commodi consequat. Quis aute iure reprehenderit in voluptate velit esse cillum dolore eu fugiat nulla pariatur. Excepteur sint obcaecat cupiditat non proident, sunt in culpa qui officia deserunt mollit anim id est laborum.</p>
</section>

<section class="panel inside-bg" style="left:670px; top:545px;">
  <div class="photo" role="img" aria-label="Photo of a modern campus building behind trees" style="top:380px; height:137px; background:linear-gradient(180deg,#9aa58f 0%,#c6c9c8 45%,#8a9488 100%);"></div>
  <svg class="layer" viewBox="0 0 244 517" preserveAspectRatio="none" aria-hidden="true">
    <path d="M0,388 Q140,345 244,340 L244,352 Q140,360 0,400 Z" fill="#2b2b2b"/>
  </svg>
  <div class="section-bar">Centre for Market Structure Studies</div>
  <h3 class="copy-heading ruled on-light" style="left:22px; top:58px;">Lorem Ipsum</h3>
  <p class="copy on-light" style="left:22px; top:86px; width:204px;">Lorem ipsum dolor sit amet, consectetur adipisici elit, sed eiusmod tempor incidunt ut labore et dolore magna aliqua. Ut enim ad minim veniam, quis nostrud exercitation ullamco laboris nisi ut aliquid ex ea commodi consequat. Quis aute iure reprehenderit in voluptate velit esse cillum dolore eu fugiat nulla pariatur. Excepteur sint obcaecat cupiditat non proident, sunt in culpa qui officia deserunt mollit anim id est laborum.</p>
  <p class="copy on-light" style="left:22px; top:228px; width:204px;">Lorem ipsum dolor sit amet, consectetur adipisici elit, sed eiusmod tempor incidunt ut labore et dolore magna aliqua. Ut enim ad minim veniam, quis nostrud exercitation ullamco laboris nisi ut aliquid ex ea commodi consequat. Quis aute iure reprehenderit in voluptate velit esse cillum dolore eu fugiat nulla pariatur. Excepteur sint obcaecat cupiditat non proident, sunt in culpa qui officia deserunt mollit anim id est laborum.</p>
</section>

<section class="panel inside-bg" style="left:914px; top:545px;">
  <div class="photo" role="img" aria-label="Photo of a large green tree on campus" style="top:305px; height:212px; background:linear-gradient(160deg,#8fb05a 0%,#5d7f32 45%,#3e4e2a 100%);"></div>
  <svg class="layer" viewBox="0 0 244 517" preserveAspectRatio="none" aria-hidden="true">
    <path d="M0,318 Q120,298 244,295 L244,318 Q120,312 0,330 Z" fill="#2b2b2b"/>
  </svg>
  <div class="section-bar">Centre for Market Structure Studies</div>
  <h3 class="copy-heading ruled on-light" style="left:28px; top:58px;">Lorem Ipsum</h3>
  <p class="copy on-light" style="left:28px; top:86px; width:200px;">Lorem ipsum dolor sit amet, consectetur adipisici elit, sed eiusmod tempor incidunt ut labore et dolore magna aliqua. Ut enim ad minim veniam, quis nostrud exercitation ullamco laboris nisi ut aliquid ex ea commodi consequat. Quis aute iure reprehenderit in voluptate velit esse cillum dolore eu fugiat nulla pariatur. Excepteur sint obcaecat cupiditat non proident, sunt in culpa qui officia deserunt mollit anim id est laborum.</p>
  <div class="name-plate dark" style="top:240px; font-size:34px;">KPL</div>
</section>

</body>
</html>
```